Book Cover: Unmaking The Hollow Reversal with KEEL-Route

I'm looking for a book cover for my pending book. I do NOT want any AI-generated image with its notoriously-slick AI imagery.
The Title is: "Unmaking The Hollow Reversal with KEEL-Route" with the lengthy added subtitle "The Roadmap to Durably Renew Our Federal Union, Beyond the Ballot Count, Nearly Instantly."
Also on the front cover--author name of "Dale Whitcomb" (lower on the cover).
Parameters or things to consider:
1. Please separate the title from the subtitle with a colon, and emphasize the title greatly over the long subtitle.
2. "The Hollow Reversal" is ultimately a "bad" thing (because it cleverly hides federal action beyond the spirit of the Constitution).
3. Since abolishing a "bad" thing is a good thing, "Abolishing" should reflect that positive note, and perhaps be larger font, perhaps slanted (symbolically cancelling then "The Hollow Reversal").
4. "KEEL-Route" is a "good" thing, too, as it's the method to end the bad thing.
5. On the subtitle, much smaller fonts to keep all that text from overwhelming the front cover.
6. Please allow 3/8" for bleed and then still keep all text well away (3/8" or more) from those trim edges.
7. The book will be 6" X 9", and probably 1" thick (~400 pages). Overall dimensions will be 13.75" WX 9 .75" H (again, 3/8" bleed X 4).
8. For the back cover, but I'll just put a white box over most of the back, and then add the text later (before print submission). Continue colors of front onto back (but no real graphic needed).
9. For the cover graphic, I was thinking that an old country road may work well, because of the relevance of the fictional metaphor that is found in Chapter 3 of this non-fiction book. However, I'm not sure if this image will prove successful (even as the story provides a great visual for the premise of the book).
10. Spine: Title and author last name only is fine (no subtitle or first name of author).
Basically, I'm thinking of a long-ago rural road, perhaps in Utah (fictionally), with generic red rock formations in the background, and largely desert views surrounding the roadway. The simple road itself needn't necessarily be paved, but no more than one lane in each direction and not a lot of modern street markings.
I prefer the approach road to the T-Intersection be more-visible -- at a closer-perspective -- as it travels from the lower left of the front cover, slightly upwards, at a growing distance, towards the right side of the book, but ending well before the book's right edge, at a formal "T-Intersection," with this crossroad at 90 degrees perpendicular to the approach road.
This crossroad then will come from the (lower) right of the book, heading somewhat slantwise to the (upper) left area of the book generally, with the approach road largely hitting the crossroad largely centered at the T-Intersection, or slightly to the right of center.
There should be some sort of simple American-styled stop sign (not necessarily modern design) in the normal position, found before the crossroad, at the right lane. No vehicles.
AFTER the crossroad, at the far side of the T-Intersection, the storyline describes a solid hard-rock wall, maybe 10' or 15' high, parallel with the crossroad, but not so insurmountable that the rock wall couldn't later be excavated/demolished and partially removed, so that the approach road would later continue forward, initially at street level, but much later even with an overpass (so plan the terrain beyond the T-Intersection accordingly, that an overpass from the approach road could continue forward from the stop sign, that currently only offers a left or right path).
In-between the far side of the crossroad and the rock wall, there should be some sort of crude arrow sign, serving as a simple notice or barrier against travelling forward, notifying people to turn either right or left.
That arrow sign pointing right could also say "Enumerated Powers" and the sign pointing left can point to "Inherent Powers".
Again, the signs should be simple (more appropriate for long-ago, rather than modern).
In the story, decades later, the rock wall gets excavated first for a ground-level road, that in time became a multi-lane formal overpass and freeway, that largely ends up hiding the old T-Intersection from open view, but importantly, NEVER REMOVES OR FULLY OBSCURES the T-Intersection, or right-path road (the overpass gets shifted a little left from the approach road [with the approach road then becoming the one-way off-ramp, down to the stop sign, from the new freeway forward]).
It may be unworkable, but perhaps the primary shaded-in view would be that initial/earliest scene described above, but perhaps a stick or outline future-vision-view (like an engineering draft, for example) could overlay or outline an overpass and formal freeway continuing forward.
Again, though, the original T-Intersection can't be fully obscured or torn down with the new freeway design, even as it could be partially obscured.
I am open though, to other ideas on the cover, but I just don't know what they would be.
The design ultimately should reflect 200 years of incremental federal treachery, imposed primarily by our courts (with improper action resting upon invalid and dishonest activity [yet when properly-challenged, may be overcome {think of Pim in The Keeper of Vell, pulling back the curtain to expose the self-proclaiming wizard of unlimited power, who was only a fraud}]).
Please note that although The Marvelous Keeper of Vell book is now in the public domain, the 1939 movie is still copyrighted (so no visuals based on the movie), in any alternate designs.
Conservative Americans interested in restoring individual liberty and limited government under the U.S. Constitution and our country's founding principles

```html
<!DOCTYPE html>
<html lang="en">
<head>
<meta charset="utf-8">
<title>Unmaking The Hollow Reversal with KEEL-Route — Cover Wrap</title>
<link rel="stylesheet" href="https://fonts.googleapis.com/css2?family=Yellowtail&family=Oswald:wght@500;600&family=Poppins:wght@400&display=swap">
<style>
  :root {
    --stage: #e7e7e9;
    --ink-dark: #140d09;
    --back-top: #1e1410;
    --back-bottom: #0e0907;
    --spine: #120c09;
    --title-brown: #2a1a10;
    --paper-white: #ffffff;
    --copy-white: #f2ece6;
    --sepia-sky: #cdb892;
    --sepia-mid: #9c7d55;
    --sepia-earth: #5a3d24;
    --sepia-deep: #2b1b10;
  }
  * { margin: 0; padding: 0; box-sizing: border-box; }
  html, body { width: 882px; height: 1200px; overflow: hidden; }
  body { background: var(--stage); position: relative; }

  .cover-wrap {
    position: absolute; left: 20px; top: 305px;
    width: 842px; height: 590px;
    display: flex;
  }

  /* Back cover */
  .back-cover {
    position: relative; width: 391px; height: 100%;
    background: radial-gradient(ellipse at 50% 25%, #2a1c15 0%, var(--back-top) 45%, var(--back-bottom) 100%);
    color: var(--copy-white);
  }
  .back-cover .script-title {
    position: absolute; left: 0; right: 0; top: 62px;
    text-align: center;
    font-family: "Yellowtail", cursive;
    font-size: 52px; line-height: 1;
    color: var(--paper-white);
    text-shadow: 0 0 6px rgba(255,255,255,.75), 0 0 14px rgba(255,255,255,.35);
  }
  .back-cover .series-line {
    position: absolute; left: 0; right: 0; top: 124px;
    text-align: center;
    font-family: "Oswald", sans-serif; font-weight: 600;
    font-size: 18px; letter-spacing: -.2px;
    color: var(--paper-white);
    text-shadow: 0 0 5px rgba(255,255,255,.6);
  }
  .series-line .connector, .front-title .connector { font-size: .55em; }
  .blurb {
    position: absolute; left: 31px; width: 329px;
    font-family: "Poppins", sans-serif;
    font-size: 7.4px; line-height: 8.8px;
    text-align: center; color: var(--copy-white);
  }
  .blurb-one { top: 178px; }
  .blurb-two { top: 248px; }
  .blurb-three { top: 290px; }
  .blurb-about { top: 488px; }
  .copy-box {
    position: absolute; left: 157px; top: 383px;
    width: 76px; height: 76px;
    background: var(--paper-white); border-radius: 9px;
  }

  /* Spine */
  .spine {
    position: relative; width: 60px; height: 100%;
    background: var(--spine);
    border-left: 1px solid #2a1d16;
  }
  .spine-title, .spine-author {
    position: absolute; left: 50%;
    transform-origin: 0 0;
    white-space: nowrap; color: var(--paper-white);
  }
  .spine-title {
    top: 48px; transform: rotate(90deg) translateY(-50%);
    font-family: "Oswald", sans-serif; font-weight: 600; font-size: 19px;
    text-shadow: 0 0 5px rgba(255,255,255,.5);
  }
  .spine-title .script { font-family: "Yellowtail", cursive; font-weight: 400; font-size: 24px; margin-right: 6px; }
  .spine-author {
    top: 486px; transform: rotate(90deg) translateY(-50%);
    font-family: "Oswald", sans-serif; font-weight: 600; font-size: 15px; letter-spacing: .5px;
  }

  /* Front cover */
  .front-cover { position: relative; width: 391px; height: 100%; overflow: hidden; }
  .front-cover .cover-art {
    position: absolute; inset: 0;
    background:
      radial-gradient(ellipse at 50% 30%, rgba(230,215,180,.55) 0%, rgba(230,215,180,0) 55%),
      linear-gradient(180deg, var(--sepia-sky) 0%, #bba27a 35%, var(--sepia-mid) 55%, var(--sepia-earth) 75%, var(--sepia-deep) 100%);
  }
  .front-cover .script-title {
    position: absolute; left: 0; right: 0; top: 34px;
    text-align: center;
    font-family: "Yellowtail", cursive;
    font-size: 80px; line-height: 1;
    color: var(--title-brown);
  }
  .front-title {
    position: absolute; left: 0; right: 0; top: 124px;
    text-align: center;
    font-family: "Oswald", sans-serif; font-weight: 600;
    font-size: 27px; line-height: 1; letter-spacing: -.3px;
    color: var(--title-brown);
  }
  .front-subtitle {
    position: absolute; left: 30px; right: 30px; top: 168px;
    text-align: center;
    font-family: "Oswald", sans-serif; font-weight: 500;
    font-size: 13.5px; line-height: 17px;
    color: var(--title-brown);
  }
  .front-author {
    position: absolute; left: 0; right: 0; top: 528px;
    text-align: center;
    font-family: "Oswald", sans-serif; font-weight: 600;
    font-size: 28px; letter-spacing: .4px;
    color: var(--paper-white);
  }
</style>
</head>
<body>
  <main class="cover-wrap">
    <section class="back-cover">
      <h2 class="script-title">Unmaking</h2>
      <p class="series-line">The Hollow Reversal <span class="connector">with</span> KEEL-Route</p>
      <p class="blurb blurb-one">For two centuries, quiet rulings have turned a charter of limited powers on its head. This book traces how that reversal took hold, names the habits that keep it standing, and lays out a plain route any citizen can follow to set the order right again.</p>
      <p class="blurb blurb-two">Written for readers who prize liberty, it asks one question: who granted the power, and where is it written down?</p>
      <p class="blurb blurb-three">Each chapter pairs history with a working step, from the first court cases to the present day. The result is a clear map, not a slogan, showing where the road was turned aside and how it can be brought back to the path the founders laid.</p>
      <div class="copy-box"></div>
      <p class="blurb blurb-about">Dale Whitcomb has spent years studying the founding debates and the cases that followed. He writes for neighbors, not lawyers, and believes the curtain can still be pulled back.</p>
    </section>

    <section class="spine">
      <p class="spine-title"><span class="script">Unmaking</span>The Hollow Reversal with KEEL-Route</p>
      <p class="spine-author">Whitcomb</p>
    </section>

    <section class="front-cover">
      <div class="cover-art" role="img" aria-label="Sepia photograph of a dirt country road running into the distance under a cloudy sky, with a wooden arrow signpost marked Enumerated Powers and Inherent Powers on the left and a red stop sign on the right"></div>
      <h1 class="script-title">Unmaking</h1>
      <p class="front-title">The Hollow Reversal <span class="connector">with</span> KEEL-Route</p>
      <p class="front-subtitle">The Roadmap to Durably Renew Our Federal Union,<br>Beyond the Ballot Count, Nearly Instantly.</p>
      <p class="front-author">Dale Whitcomb</p>
    </section>
  </main>
</body>
</html>
```